Surgical Conditions of the thyroid and parathyroid glands - a flyer for GPs

Hi there,

I am a thyroid surgeon trying to produce a bi-fold A4 flyer as a quick reference guide for general practitioners (family doctors). It needs to feel friendly and professional.

The text for the four "pages" can be found in the "thyroid flyer for design" document attached.

The front page should have:
- The title
- the photo with the patient having an ultrasound
- the photo of the asian woman with the enlarged thyroid gland
- possibly the photo of the blonde woman touching her neck

The inner two pages are predominantly text - I would love this to be presented in an easy to read, uncluttered format. There is a photo attached which demonstrates the parathyroid glands. This should be placed near the parathyroid text section if possible.

The back page is a brief bio of myself. It should have the profile pic attached.
It should have contact details, which I forgot to put in the word document. These details are:
Phone (03) 9482 5170 for all appointments
Consulting at:
18 Wattlebird Lane, Berwick, VIC 3806
hollowaymedicalteam.com.au
dorianpelsworth.com

The back page should also have the "Tarrow Care" and "Guild of Operators" logos.

If possible, all pages should have the "Holloway Medical Team" logo.

The whole feel could have a similar colour scheme to my group website (largely orange and green). Please see www.hollowaymedicalteam.com.au for examples.

Many thanks!

Target Market(s)

General practitioners (ie family doctors)

Industry/Entity Type

Medical And Science

Font styles to use
Sans Serif

Colors
33b8a4
f78f20

Requirements
Must have
• Contact details on the back, holloway medical team logo on front and back pages, Tarrow Care and Guild of Operators logo on the back.
Nice to have
• Other medical/surgical related images as you see fit - sorry to be so broad!!

```html
<!DOCTYPE html>
<html lang="en">
<head>
<meta charset="utf-8">
<title>Surgical Conditions of the Thyroid and Parathyroid Glands – Quick Reference Guide for GPs</title>
<link href="https://fonts.googleapis.com/css2?family=Open+Sans:wght@400;600;700;800&display=swap" rel="stylesheet">
<style>
  :root {
    --orange: #f78f20;
    --orange-deep: #e0822a;
    --teal: #33b8a4;
    --teal-soft: #5fb5a6;
    --ink: #3a3a3a;
    --paper: #ffffff;
    --stage: #e9e9ea;
    --photo-grey: #d9d7de;
  }
  * { margin: 0; padding: 0; box-sizing: border-box; }
  html, body {
    width: 1200px; height: 789px; overflow: hidden;
    background: var(--stage);
    font-family: "Open Sans", Arial, sans-serif;
  }
  .cover {
    position: absolute; left: 340px; top: 26px;
    width: 520px; height: 736px;
    background: var(--paper);
    overflow: hidden;
    box-shadow: 0 2px 10px rgba(0,0,0,.12);
  }
  .cover-art { position: absolute; inset: 0; width: 520px; height: 736px; }
  .title-block {
    position: absolute; left: 236px; top: 388px; width: 276px;
    color: var(--ink);
  }
  .title-kicker { font-size: 18px; font-weight: 400; letter-spacing: .2px; line-height: 1.2; }
  .title-main {
    font-size: 23px; font-weight: 800; color: var(--paper);
    line-height: 1.05; letter-spacing: .3px; margin: 3px 0 5px;
  }
  .title-sub { font-size: 16px; font-weight: 400; line-height: 1.3; letter-spacing: .2px; }
  .brand {
    position: absolute; left: 104px; top: 628px; width: 170px;
    display: flex; flex-direction: column; align-items: center; gap: 8px;
  }
  .brand-dot { width: 30px; height: 30px; border-radius: 50%; background: var(--orange); }
  .brand-name {
    font-size: 20px; font-weight: 700; color: var(--ink);
    line-height: 1.1; text-align: center;
  }
  .site-url {
    position: absolute; right: 22px; bottom: 20px;
    font-size: 12.5px; font-weight: 600; color: var(--ink);
  }
  .site-url span { color: var(--orange); }
</style>
</head>
<body>
  <main class="cover">
    <svg class="cover-art" viewBox="0 0 520 736" xmlns="http://www.w3.org/2000/svg">
      <defs>
        <linearGradient id="heroTone" x1="0" y1="0" x2="1" y2=".6">
          <stop offset="0" stop-color="#a37f62"/>
          <stop offset=".28" stop-color="#e4c4b2"/>
          <stop offset=".55" stop-color="#edd6ca"/>
          <stop offset=".8" stop-color="var(--photo-grey)"/>
          <stop offset="1" stop-color="#d0ced6"/>
        </linearGradient>
        <radialGradient id="goitreTone" cx=".5" cy=".45" r=".65">
          <stop offset="0" stop-color="#b48a60"/>
          <stop offset=".8" stop-color="#7e5d40"/>
          <stop offset="1" stop-color="#c98a8a"/>
        </radialGradient>
        <linearGradient id="scanTone" x1="0" y1="0" x2="1" y2="1">
          <stop offset="0" stop-color="#e8e6ea"/>
          <stop offset=".5" stop-color="#c9b8ae"/>
          <stop offset="1" stop-color="#eeecef"/>
        </linearGradient>
        <linearGradient id="orangeTone" x1="0" y1="0" x2="1" y2="0">
          <stop offset="0" stop-color="var(--orange-deep)"/>
          <stop offset="1" stop-color="var(--orange)"/>
        </linearGradient>
      </defs>

      <rect class="teal-field" x="0" y="0" width="520" height="736" fill="var(--teal-soft)"/>

      <path class="hero-photo" d="M0 0 H520 V232 C 380 268 240 330 150 400 C 100 435 50 452 0 458 Z"
            fill="url(#heroTone)" role="img" aria-label="Photo of a woman touching the front of her neck"/>

      <path class="panel-orange" d="M520 258 C 400 292 270 360 200 452 C 250 560 380 594 520 604 Z" fill="url(#orangeTone)"/>

      <path class="panel-white" d="M62 736 C 60 650 130 606 240 612 C 340 618 440 632 520 638 L520 736 Z" fill="var(--paper)"/>

      <circle cx="118" cy="478" r="84" fill="url(#goitreTone)" stroke="var(--teal-soft)" stroke-width="8"
              role="img" aria-label="Photo of a patient with an enlarged thyroid gland"/>
      <circle cx="414" cy="610" r="56" fill="url(#scanTone)" stroke="var(--orange)" stroke-width="6"
              role="img" aria-label="Photo of a patient having a neck ultrasound"/>
    </svg>

    <header class="title-block">
      <p class="title-kicker">SURGICAL CONDITIONS</p>
      <h1 class="title-main">OF THE THYROID<br>AND PARATHYROID<br>GLANDS</h1>
      <p class="title-sub">A QUICK REFERENCE GUIDE<br>FOR GPs</p>
    </header>

    <div class="brand">
      <span class="brand-dot"></span>
      <span class="brand-name">Holloway<br>Medical Team</span>
    </div>

    <p class="site-url">www.<span>hollowaymedicalteam</span>.com.au</p>
  </main>
</body>
</html>
```